Create Awesome Sale/AD graphics for BLACK FRIDAY

Create a (3) Black Friday graphics integrating our supplied pictures .
Text requirements = Black Friday/Cyber Monday sale
Text requirements = Deals up to 50% off
Text requirements = www.BLUMORAK.co
Integrate Blu Morak Logo

We would like to drop these graphics into a video, and use for Social Medai post's we would like perimeter around the graphic to be dark to fit the theme the graphic will be added at @15-17 sec in this video:
Youtube Video this Ad is live for this request here:
https://www.vidplexa.com/watch?v=ZqT4mLw8RbE

I will upload a series of images we would like to use, choose the three you like to use.

Typically when we have graphics generated we get a zip file of the graphics in these formats EPS/AI/PDF/JPEG/PNG

Target Market(s)

Fishing, 50% mix male/female, ages 18-35

Colors

Designer to choose colors to be used in the design.

Requirements
Must have
• Create a (3) Black Friday graphics integrating our supplied pictures .
• Text requirements = Black Friday/Cyber Monday sale
• Text requirements = Deals up to 50% off
• Text requirements = www.BLUMORAK.co
• Integrate Blu Morak Logo
• ** I have more Blu Morak EPS/AI if needed See attached
Nice to have
• We would like to drop these graphics into a video, and use for Social Medai post's we would like perimeter around the graphic to be dark tto fit the theme the graphic will be added at @15-17 sec in this video:
• Youtube Video this Ad is live for this request here:
• https://www.vidplexa.com/watch?v=ZqT4mLw8RbE
Should not have
• a lot of white space

```html
<!DOCTYPE html>
<html lang="en">
<head>
<meta charset="utf-8">
<title>Blu Morak Black Friday Set</title>
<link rel="stylesheet" href="https://fonts.googleapis.com/css2?family=Anton&family=Montserrat:wght@700;900&family=Oswald:wght@500;700&display=swap">
<style>
:root{
  --stage:#d9d9d9;
  --ink:#15171c;
  --ink-2:#23262d;
  --red:#e01b22;
  --red-dark:#a50f14;
  --white:#ffffff;
}
*{margin:0;padding:0;box-sizing:border-box}
html,body{width:1200px;height:316px;overflow:hidden;background:var(--stage)}
.canvas{position:relative;width:1200px;height:316px}
.ad{position:absolute;top:18px;width:265px;height:265px;overflow:hidden;
  background:linear-gradient(160deg,var(--ink-2),var(--ink) 60%);color:var(--white)}
.ad--one{left:27px}.ad--two{left:319px}.ad--three{left:611px}.ad--four{left:904px}
.photo{position:absolute}
.brand{position:absolute;font-family:"Oswald",sans-serif;font-weight:700;font-size:11px;line-height:1;
  letter-spacing:1.5px;color:var(--white);text-transform:uppercase;display:flex;align-items:center;gap:5px;white-space:nowrap}
.brand::before{content:"";width:7px;height:7px;background:var(--white)}
.url{position:absolute;font-family:"Oswald",sans-serif;font-weight:500;font-size:7.5px;line-height:1;letter-spacing:.4px;white-space:nowrap}

/* panel one */
.one-block{position:absolute;left:14px;top:0;width:130px;height:133px;background:var(--red)}
.one-frame{position:absolute;left:7px;top:20px;width:143px;height:98px;border:1.5px solid var(--white)}
.one-url{left:22px;top:6px;font-family:"Montserrat",sans-serif;font-weight:700;font-size:6px;letter-spacing:1.2px}
.one-title{position:absolute;left:18px;top:24px;font-family:"Montserrat",sans-serif;font-weight:900;
  font-size:33px;line-height:1.05;letter-spacing:-1px}
.one-sub{position:absolute;left:20px;top:101px;font-family:"Oswald",sans-serif;font-weight:700;font-size:19px;line-height:1;letter-spacing:5px}
.one-fifty{position:absolute;left:14px;top:128px;font-family:"Oswald",sans-serif;font-weight:700;font-size:108px;
  line-height:1;color:var(--red);letter-spacing:-4px}
.one-upto{position:absolute;left:112px;top:138px;font-family:"Oswald",sans-serif;font-weight:700;font-size:30px;line-height:.95}
.one-pct{position:absolute;left:112px;top:198px;font-family:"Oswald",sans-serif;font-weight:700;font-size:32px;line-height:1;color:var(--red)}
.one-off{position:absolute;left:14px;top:238px;width:130px;height:27px;background:var(--red);
  font-family:"Oswald",sans-serif;font-weight:700;font-size:21px;text-align:center;line-height:27px;letter-spacing:2px}

/* panels two & three */
.diamond{position:absolute;left:0;top:0}
.bf-black{position:absolute;left:104px;top:32px;font-family:"Anton",sans-serif;font-size:62px;line-height:1;color:var(--red)}
.bf-friday{position:absolute;left:120px;top:96px;font-family:"Oswald",sans-serif;font-weight:500;font-size:46px;line-height:1;letter-spacing:-1.5px}
.bf-discount{position:absolute;left:146px;top:148px;font-family:"Oswald",sans-serif;font-weight:500;font-size:18px;line-height:1}
.tag{position:absolute;left:205px;top:202px;width:44px;height:30px;background:var(--white);color:var(--red);
  transform:rotate(40deg);border-radius:3px;font-family:"Oswald",sans-serif;font-weight:700;display:flex;align-items:center;justify-content:center;gap:2px}
.tag b{font-size:17px;line-height:1}
.tag span{font-size:5px;line-height:1.05;color:var(--ink)}

/* panel four */
.four-title{position:absolute;left:8px;top:70px;transform:rotate(-22deg);transform-origin:left top}
.four-black{font-family:"Anton",sans-serif;font-size:56px;line-height:1;color:var(--white);display:block}
.four-friday{font-family:"Anton",sans-serif;font-size:38px;line-height:1;color:var(--white);display:block;margin-left:38px}
.four-ribbon{display:inline-block;margin-left:56px;margin-top:2px;background:var(--red);padding:1px 10px;
  font-family:"Oswald",sans-serif;font-weight:700;font-size:15px;line-height:1.2}
.four-tag{position:absolute;left:13px;top:172px;width:46px;height:70px;background:var(--white);border-radius:4px;
  transform:rotate(-6deg);font-family:"Oswald",sans-serif;font-weight:700;text-align:center;color:var(--ink);padding-top:9px;line-height:1}
.four-tag .t1{font-size:12px;display:block}
.four-tag .t2{font-size:24px;color:var(--red);display:block}
.four-tag .t3{font-size:16px;display:block}
</style>
</head>
<body>
<main class="canvas">

  <section class="ad ad--one">
    <div class="photo" role="img" aria-label="Angler in plaid shirt and cap holding a large salmon on a boat"
      style="left:159px;top:56px;width:106px;height:209px;background:linear-gradient(180deg,#6d7686,#3b4352 55%,#5b7899)"></div>
    <div class="one-block"></div>
    <div class="one-frame"></div>
    <span class="url one-url">www.BLUMORAK.co</span>
    <h2 class="one-title">BLACK<br>FRIDAY</h2>
    <p class="one-sub">DISCOUNT</p>
    <p class="one-fifty">50</p>
    <p class="one-upto">UP<br>TO</p>
    <p class="one-pct">%</p>
    <p class="one-off">- OFF -</p>
    <span class="brand" style="left:176px;top:38px">Blu Morak</span>
  </section>

  <section class="ad ad--two">
    <div class="photo" role="img" aria-label="Angler in cap holding a steelhead trout, blue monochrome"
      style="left:0;top:100px;width:200px;height:165px;background:linear-gradient(180deg,#3c4659,#232a36 60%,#5b6373)"></div>
    <svg class="diamond" width="265" height="265" viewBox="0 0 265 265"><polygon points="175,8 266,99 175,190 84,99" fill="none" stroke="var(--red)" stroke-width="1.5"/></svg>
    <span class="brand" style="left:13px;top:38px">Blu Morak</span>
    <h2 class="bf-black">BLACK</h2>
    <p class="bf-friday">FRIDAY</p>
    <p class="bf-discount">DISCOUNT</p>
    <div class="tag"><b>50</b><span>UP<br>TO<br>%OFF</span></div>
    <span class="url" style="left:200px;top:251px">www.BLUMORAK.co</span>
  </section>

  <section class="ad ad--three">
    <div class="photo" role="img" aria-label="Angler in cap holding a rainbow trout over a river"
      style="left:0;top:100px;width:200px;height:165px;background:linear-gradient(180deg,#4a5262,#2c3340 55%,#8c8f86)"></div>
    <svg class="diamond" width="265" height="265" viewBox="0 0 265 265"><polygon points="175,8 266,99 175,190 84,99" fill="none" stroke="var(--red)" stroke-width="1.5"/></svg>
    <span class="brand" style="left:13px;top:38px">Blu Morak</span>
    <h2 class="bf-black">BLACK</h2>
    <p class="bf-friday">FRIDAY</p>
    <p class="bf-discount">DISCOUNT</p>
    <div class="tag"><b>50</b><span>UP<br>TO<br>%OFF</span></div>
    <span class="url" style="left:200px;top:251px">www.BLUMORAK.co</span>
  </section>

  <section class="ad ad--four">
    <div class="photo" role="img" aria-label="Angler in waders kneeling in a river with a steelhead"
      style="left:60px;top:120px;width:205px;height:145px;background:linear-gradient(200deg,#7c8a6c,#9aa6a8 35%,#2e3646 70%)"></div>
    <svg style="position:absolute;left:0;top:0" width="265" height="265" viewBox="0 0 265 265">
      <polygon points="61,0 150,0 104,17" fill="var(--red)"/>
      <polygon points="2,75 160,12 172,80 12,142" fill="none" stroke="var(--white)" stroke-width="1.2"/>
    </svg>
    <div class="four-title">
      <span class="four-black">BLACK</span>
      <span class="four-friday">FRIDAY</span>
      <span class="four-ribbon">DISCOUNT</span>
    </div>
    <span class="brand" style="left:178px;top:38px">Blu Morak</span>
    <div class="four-tag"><span class="t1">UP TO</span><span class="t2">50%</span><span class="t3">OFF</span></div>
    <span class="url" style="left:10px;top:251px">www.BLUMORAK.co</span>
  </section>

</main>
</body>
</html>
```